Fun Language School in San Diego, CA - We want cool Business Card

We need a new business card design for our new logo. We are a language school in beautiful San Diego, California. Our target is students from all over the world who age from 18 to 25. They come to our school to learn English. Our school has a modern look, trending and fun place. We are the only language school who use tablets in class. We are student oriented, Students Come First is our slogan. We are re-branding ourselves with a new logo. We would like to see a designs that use our new logo and it should reflect the feel of young, fun, modern, high-tech and attractive to young people.
I've seen some business card designs with transparent look, unusual shapes, we are open to any cool ideas. Thank you very much!

In order for you to know more about our school, here are the links to our Youtube Channel and Facebook.

Youtube: https://www.vidmarlo.example/channel/ZXpolrT-48kwb2nH7c5DqLm
Facebook: https://www.friendlane.example/BVSchool

Target Market(s)

Our target is students from all over the world who age from 18 to 25. International students.

Industry/Entity Type

School

Font styles to use
Sans Serif

Requirements
Must have
• Our new logo. Name, title and address.
Should not have
• Other colors other than the ones we have in our logo. Characters are fine.

```html
<!DOCTYPE html>
<html lang="en">
<head>
<meta charset="utf-8">
<title>BV International School – Business Card</title>
<link rel="stylesheet" href="https://fonts.googleapis.com/css2?family=Arimo:wght@400;700&display=swap">
<style>
  :root {
    --backdrop: #e00612;
    --band: #0d0d10;
    --paper: #ffffff;
    --ink: #111111;
    --rule: #333333;
    --mark-teal: #05a9b5;
    --on-band: #ffffff;
  }
  * { margin: 0; padding: 0; box-sizing: border-box; }
  html, body { width: 1200px; height: 1000px; overflow: hidden; }
  body {
    background: var(--backdrop);
    font-family: "Arimo", Arial, sans-serif;
    color: var(--ink);
    position: relative;
  }
  .card {
    position: absolute;
    left: 225px; top: 280px;
    width: 749px; height: 439px;
    background: var(--paper);
    border-radius: 72px 0 72px 0;
    overflow: hidden;
  }
  .card__band {
    position: absolute; left: 0; top: 0;
    width: 100%; height: 241px;
    background: var(--band);
  }
  .brand__dot {
    position: absolute;
    left: 18px; top: 42px;
    width: 176px; height: 176px;
    border-radius: 50%;
    background: var(--mark-teal);
  }
  .brand__name {
    position: absolute;
    left: 238px; top: 92px;
    color: var(--on-band);
    font-weight: 400;
    line-height: 1;
  }
  .brand__name .line-1 { display: block; font-size: 52px; }
  .brand__name .line-2 { display: block; font-size: 40px; margin: 14px 0 0 28px; }
  .holder {
    position: absolute;
    left: 103px; top: 298px;
  }
  .holder__name { font-size: 22px; font-weight: 400; }
  .holder__name strong { font-weight: 700; }
  .holder__title { font-size: 19px; margin-top: 6px; }
  .divider {
    position: absolute;
    left: 381px; top: 252px;
    width: 2px; height: 187px;
    background: var(--rule);
  }
  .contact {
    position: absolute;
    left: 411px; top: 266px;
    font-size: 20px;
    line-height: 28px;
    font-style: normal;
  }
  .contact .gap { margin-top: 8px; }
  .contact .label { display: inline-block; width: 28px; }
</style>
</head>
<body>
  <article class="card">
    <header class="card__band">
      <span class="brand__dot" aria-hidden="true"></span>
      <div class="brand__name">
        <span class="line-1">BV International</span>
        <span class="line-2">School</span>
      </div>
    </header>
    <div class="holder">
      <p class="holder__name">Marcus <strong>Ellery</strong></p>
      <p class="holder__title">Principle</p>
    </div>
    <span class="divider" aria-hidden="true"></span>
    <address class="contact">
      <div>2740 Harbor Ave, Ste 210</div>
      <div>San Diego, CA 92103</div>
      <div class="gap"><span class="label">P:</span>+1.619.555.0148</div>
      <div><span class="label">F:</span>619.555.0172</div>
      <div><span class="label">E:</span>info@bvschool.example</div>
    </address>
  </article>
</body>
</html>
```